Refresh of The Marston Collective business card

Update business card design using existing primary logo. Names, numbers, etc. are too hard to read on current design.

Target Market(s)

We are a CPA firm.

Industry/Entity Type

Accountant

Contact Information for Business Card

update current card

Colors
0355a3
3176b5
85acd3
0792cd

Requirements
Must have
• Easier to read phone numbers and names
• Use existing logo
Nice to have
• We love our color scheme and current TMC logo. But the names and phone numbers are too small and card just look old and stale.

```html
<!DOCTYPE html>
<html lang="en">
<head>
<meta charset="utf-8">
<title>The Marston Collective – Business Card</title>
<link rel="stylesheet" href="https://fonts.googleapis.com/css2?family=Open+Sans:wght@400;600;700&display=swap">
<style>
  :root {
    --backdrop: #4a4340;
    --card-white: #fbfbfb;
    --card-black: #111111;
    --brand-navy: #0355a3;
    --brand-blue: #3176b5;
    --ink: #2a2a2a;
    --divider: #d6d6d6;
    --silver: #c9c9c9;
  }
  * { box-sizing: border-box; margin: 0; padding: 0; }
  html, body { width: 1200px; height: 900px; overflow: hidden; }
  body {
    background: var(--backdrop);
    font-family: "Open Sans", Arial, sans-serif;
    position: relative;
  }
  .card {
    position: absolute;
    top: 307px;
    width: 500px;
    height: 286px;
    overflow: hidden;
    box-shadow: 0 10px 26px rgba(0,0,0,0.45);
  }
  .card--front { left: 70px; background: var(--card-white); }
  .card--back  { left: 630px; background: var(--card-black); }

  /* Front */
  .front-mark {
    position: absolute;
    left: 0; top: 0; width: 230px; height: 100%;
    display: flex; flex-direction: column; align-items: center; justify-content: center; gap: 14px;
  }
  .front-mark__disc {
    width: 130px; height: 130px; border-radius: 50%;
    background: var(--brand-navy);
  }
  .front-mark__name {
    font-weight: 600; font-size: 20px;
    color: var(--brand-navy);
  }
  .front-divider {
    position: absolute; left: 232px; top: 70px; bottom: 40px;
    width: 1px; background: var(--divider);
  }
  .front-details { position: absolute; left: 258px; top: 38px; right: 14px; color: var(--ink); }
  .person-name { font-weight: 700; font-size: 18px; color: var(--brand-navy); margin-bottom: 16px; }
  .address { font-size: 14px; line-height: 1.35; margin-bottom: 16px; }
  .contact-list { list-style: none; font-size: 14px; line-height: 1.5; }
  .contact-list li { display: flex; align-items: center; gap: 8px; }
  .contact-list svg { width: 12px; height: 12px; fill: var(--brand-navy); flex: none; }

  /* Back */
  .back-lockup {
    position: absolute; left: 70px; top: 80px;
    display: flex; align-items: center; gap: 18px;
  }
  .back-lockup__disc {
    width: 90px; height: 90px; border-radius: 50%;
    background: var(--silver);
    flex: none;
  }
  .firm-name {
    font-weight: 600; font-size: 22px;
    color: var(--silver);
    white-space: nowrap;
  }
  .website {
    position: absolute; left: 0; right: 0; top: 210px;
    text-align: center; font-size: 15px; font-weight: 600; color: var(--silver);
  }
</style>
</head>
<body>
  <section class="card card--front" aria-label="Business card front">
    <div class="front-mark">
      <div class="front-mark__disc"></div>
      <p class="front-mark__name">TMC</p>
    </div>
    <div class="front-divider"></div>
    <div class="front-details">
      <p class="person-name">Daniel R. Marston, CPA</p>
      <p class="address">812 Lindell Ave. Suite 310<br>Oakridge, Florida 32099</p>
      <ul class="contact-list">
        <li><svg viewBox="0 0 12 12" aria-hidden="true"><path d="M2.5 1 L4.5 1 L5.3 3.6 L4 4.6 C4.7 6 6 7.3 7.4 8 L8.4 6.7 L11 7.5 L11 9.5 C11 10.3 10.3 11 9.5 11 C5 11 1 7 1 2.5 C1 1.7 1.7 1 2.5 1 Z"/></svg>555.214.3087</li>
        <li><svg viewBox="0 0 12 12" aria-hidden="true"><rect x="3" y="1" width="6" height="3"/><rect x="1" y="4" width="10" height="5" rx="1"/><rect x="3" y="8" width="6" height="3"/></svg>555.214.3090</li>
        <li><svg viewBox="0 0 12 12" aria-hidden="true"><path d="M3 0.5 H9 A1 1 0 0 1 10 1.5 V10.5 A1 1 0 0 1 9 11.5 H3 A1 1 0 0 1 2 10.5 V1.5 A1 1 0 0 1 3 0.5 Z M3.2 2 V9 H8.8 V2 Z"/></svg>555.671.2248</li>
        <li><svg viewBox="0 0 12 12" aria-hidden="true"><path d="M0.5 2.5 H11.5 V9.5 H0.5 Z M1.2 3 L6 6.6 L10.8 3 Z" fill-rule="evenodd"/></svg>dan@marstoncollective.com</li>
      </ul>
    </div>
  </section>

  <section class="card card--back" aria-label="Business card back">
    <div class="back-lockup">
      <div class="back-lockup__disc"></div>
      <p class="firm-name">The Marston Collective</p>
    </div>
    <p class="website">www.marstoncollective.com</p>
  </section>
</body>
</html>
```